Bloom Ferry Kite Business cards

Logo, tag line and photo on card
Agent Name
Title
Address
Phone number
Email
Website
Make logo on one side large by rotating  to portrait format.  Keep the background of the logo white.

Contact Information for Business Card
Slogan; Keeping Each Kite Aloft

```html
<!DOCTYPE html>
<html lang="en">
<head>
<meta charset="utf-8">
<title>Bloom Ferry Kite Business Cards</title>
<link href="https://fonts.googleapis.com/css2?family=Montserrat:wght@400;500;700;800&display=swap" rel="stylesheet">
<style>
  :root {
    --navy: #06236a;
    --red: #c8141e;
    --white: #ffffff;
    --stage: #e9e9ec;
  }
  * { box-sizing: border-box; margin: 0; padding: 0; }
  html, body { width: 1200px; height: 878px; overflow: hidden; }
  body {
    background: var(--stage);
    font-family: "Montserrat", sans-serif;
    position: relative;
  }
  .card {
    position: absolute;
    top: 159px;
    width: 340px;
    height: 560px;
    border-radius: 34px;
    overflow: hidden;
    background: var(--navy);
    box-shadow: 0 6px 18px rgba(0,0,0,0.18);
  }
  .card--front { left: 220px; }
  .card--back { left: 640px; }

  .logo-panel {
    position: absolute;
    background: var(--white);
    border-radius: 14px;
    display: flex;
    align-items: center;
    justify-content: center;
  }
  .logo-frame {
    width: 100%;
    height: 100%;
    border: 5px solid var(--red);
    border-radius: 14px;
    display: flex;
    flex-direction: column;
    justify-content: center;
    padding-left: 18px;
    background: var(--white);
  }
  .logo-word {
    color: var(--navy);
    font-weight: 800;
    font-size: 50px;
    line-height: 1.02;
    letter-spacing: -1px;
  }
  .card--front .logo-panel {
    left: 46px;
    top: 120px;
    width: 248px;
    height: 300px;
  }

  .back-top {
    position: absolute;
    left: 0; top: 0;
    width: 100%;
    height: 190px;
    background: var(--white);
  }
  .back-stripe {
    position: absolute;
    left: 0; top: 184px;
    width: 100%;
    height: 3px;
    background: var(--red);
  }
  .card--back .logo-panel {
    left: 80px;
    top: 40px;
    width: 210px;
    height: 250px;
    padding: 8px;
  }
  .card--back .logo-frame { padding-left: 14px; }
  .card--back .logo-word { font-size: 42px; }

  .contact {
    position: absolute;
    left: 0; top: 312px;
    width: 100%;
    text-align: center;
    color: var(--white);
  }
  .person-name {
    font-weight: 800;
    font-size: 18px;
    letter-spacing: 0.5px;
  }
  .person-title {
    font-weight: 400;
    font-size: 14px;
    margin-top: 2px;
  }
  .icon-row {
    display: flex;
    justify-content: center;
    gap: 18px;
    margin: 14px 0 10px;
  }
  .icon {
    width: 24px; height: 24px;
    border-radius: 50%;
    background: var(--white);
    display: flex; align-items: center; justify-content: center;
  }
  .contact-line {
    font-size: 13px;
    line-height: 1.5;
  }
  .divider {
    width: 210px;
    height: 1px;
    background: var(--white);
    margin: 12px auto;
  }
  .address { font-size: 13px; line-height: 1.5; }
</style>
</head>
<body>

<section class="card card--front" aria-label="Card front">
  <div class="logo-panel">
    <div class="logo-frame">
      <span class="logo-word">Bloom</span>
      <span class="logo-word">Ferry</span>
      <span class="logo-word">Kite</span>
    </div>
  </div>
</section>

<section class="card card--back" aria-label="Card back">
  <div class="back-top"></div>
  <div class="back-stripe"></div>
  <div class="logo-panel">
    <div class="logo-frame">
      <span class="logo-word">Bloom</span>
      <span class="logo-word">Ferry</span>
      <span class="logo-word">Kite</span>
    </div>
  </div>

  <div class="contact">
    <p class="person-name">DORIAN HALE</p>
    <p class="person-title">Co-Founder &amp; CEO</p>
    <div class="icon-row">
      <span class="icon" aria-label="Phone">
        <svg width="14" height="14" viewBox="0 0 24 24"><path fill="#06236a" d="M6.6 10.8a15 15 0 0 0 6.6 6.6l2.2-2.2c.3-.3.7-.4 1-.2 1.1.4 2.3.6 3.6.6.6 0 1 .4 1 1V20c0 .6-.4 1-1 1A17 17 0 0 1 3 4c0-.6.4-1 1-1h3.5c.6 0 1 .4 1 1 0 1.3.2 2.5.6 3.6.1.3 0 .7-.2 1z"/></svg>
      </span>
      <span class="icon" aria-label="Email">
        <svg width="14" height="14" viewBox="0 0 24 24"><rect x="2" y="5" width="20" height="14" rx="2" fill="#06236a"/><path d="M3 6l9 7 9-7" fill="none" stroke="#fff" stroke-width="1.8"/></svg>
      </span>
      <span class="icon" aria-label="Website">
        <svg width="14" height="14" viewBox="0 0 24 24" fill="none" stroke="#06236a" stroke-width="2"><circle cx="12" cy="12" r="9"/><path d="M3 12h18M12 3c3 3 3 15 0 18M12 3c-3 3-3 15 0 18"/></svg>
      </span>
    </div>
    <p class="contact-line">555-0142-36180</p>
    <p class="contact-line">hello@bloomferrykite.com</p>
    <p class="contact-line">www.bloomferrykite.com</p>
    <div class="divider"></div>
    <p class="address">18 Harbor Willow Lane<br>Millbrook, ME 04011 USA</p>
  </div>
</section>

</body>
</html>
```